azure haven of northeast florida business card

I need a new attractive business card. I am planning on printing on very thick rounded corner stock and having painted edges. We are a swimming pool remodel, repair, and service company in north florida. Our current logo is red, white, and blue. It doesn't necessarily have to stay that way, I am open to other ideas. It will need to contain my name, work and cell numbers, email, website, and my contractor license number.

Target Market(s)

High end residential and commercial clients

Industry/Entity Type

Business

Contact Information for Business Card

Company name, employee name and title, work and cell phone numbers, email and website, and Contractor number.

our work scope should be on card somewhere: remodel ~ repair ~ service

logo or slight variation of logo also. (not necessarily set on keeping exact logo)

Colors

Designer to choose colors to be used in the design.

Requirements
Nice to have
• We deal with water so I think some sort of water element or just a color similar to pool water would be nice to integrate into design.

```html
<!DOCTYPE html>
<html lang="en">
<head>
<meta charset="utf-8">
<title>Azure Haven of Northeast Florida — Business Card</title>
<link rel="stylesheet" href="https://fonts.googleapis.com/css2?family=Old+Standard+TT:wght@700&family=Open+Sans:wght@400;600;700&display=swap">
<style>
  :root {
    --backdrop: #c9ccd0;
    --water-light: #cdf1fa;
    --water-mid: #aee7f6;
    --water-deep: #9adcf0;
    --edge-blue: #1aa2ee;
    --edge-cyan: #35e3f7;
    --brand-navy: #1b2f9e;
    --accent-red: #d8242f;
    --title-sky: #3aa8e6;
    --license-sky: #7cc6ec;
    --contact-navy: #1e3a8f;
  }
  * { box-sizing: border-box; margin: 0; padding: 0; }
  html, body { width: 1200px; height: 910px; overflow: hidden; background: var(--backdrop); }
  .canvas { position: relative; width: 1200px; height: 910px; }

  .card {
    position: absolute;
    width: 540px;
    height: 310px;
    border-radius: 38px;
    overflow: hidden;
  }
  .card--front { left: 70px; top: 120px; }
  .card--back { left: 590px; top: 480px; }

  .card__water {
    position: absolute; inset: 0;
    background:
      radial-gradient(ellipse at 30% 30%, var(--water-light) 0%, transparent 60%),
      radial-gradient(ellipse at 75% 70%, var(--water-light) 0%, transparent 55%),
      linear-gradient(135deg, var(--water-mid), var(--water-deep));
  }
  .card__edge { position: absolute; inset: 0; width: 100%; height: 100%; }

  .wordmark { position: absolute; display: flex; align-items: center; }
  .wordmark__dot { border-radius: 50%; background: var(--accent-red); flex: none; }
  .wordmark__name {
    font-family: "Old Standard TT", "Times New Roman", serif;
    font-weight: 700;
    color: var(--brand-navy);
    text-transform: uppercase;
    line-height: 1.05;
  }
  .wordmark__line { display: block; }

  .card--front .wordmark { left: 58px; top: 100px; }
  .card--front .wordmark__dot { width: 70px; height: 70px; margin-right: 18px; }
  .card--front .wordmark__main { font-size: 44px; letter-spacing: 4px; }
  .card--front .wordmark__sub { font-size: 19px; letter-spacing: 5.5px; margin-top: 4px; }

  .scope {
    position: absolute; left: 0; right: 0; top: 236px;
    text-align: center;
    font-family: "Open Sans", Arial, sans-serif;
    font-weight: 600; font-size: 19px;
    color: var(--brand-navy);
  }

  .card--back .wordmark { left: 36px; top: 40px; }
  .card--back .wordmark__dot { width: 46px; height: 46px; margin-right: 10px; }
  .card--back .wordmark__main { font-size: 25px; letter-spacing: 2.5px; }
  .card--back .wordmark__sub { font-size: 11px; letter-spacing: 3px; margin-top: 2px; }

  .person { position: absolute; left: 40px; top: 190px; font-family: "Open Sans", Arial, sans-serif; }
  .person__name { font-size: 30px; font-weight: 700; color: var(--brand-navy); line-height: 1.1; }
  .person__first { color: var(--accent-red); }
  .person__title { font-size: 21px; color: var(--title-sky); line-height: 1.15; }
  .person__license { font-size: 14px; color: var(--license-sky); margin-left: 44px; }

  .contacts {
    position: absolute; right: 40px; top: 150px;
    list-style: none;
    font-family: "Open Sans", Arial, sans-serif;
    font-size: 13.5px; color: var(--contact-navy);
  }
  .contacts__item { display: flex; align-items: center; height: 22px; }
  .contacts__icon { width: 13px; height: 13px; margin-right: 8px; flex: none; }
</style>
</head>
<body>
<main class="canvas">

  <section class="card card--front" aria-label="Business card front">
    <div class="card__water" role="img" aria-label="Pool water surface with rippling light"></div>
    <svg class="card__edge" viewBox="0 0 540 310" aria-hidden="true">
      <rect x="8" y="8" width="524" height="294" rx="32" fill="none" stroke="var(--edge-blue)" stroke-width="16"/>
      <rect x="8" y="8" width="524" height="294" rx="32" fill="none" stroke="var(--edge-cyan)" stroke-width="16" stroke-dasharray="34 34"/>
    </svg>
    <div class="wordmark">
      <span class="wordmark__dot"></span>
      <span class="wordmark__name">
        <span class="wordmark__line wordmark__main">Azure Haven</span>
        <span class="wordmark__line wordmark__sub">of Northeast Florida</span>
      </span>
    </div>
    <p class="scope">remodel ~ repair ~ service</p>
  </section>

  <section class="card card--back" aria-label="Business card back">
    <div class="card__water" role="img" aria-label="Pool water surface with rippling light"></div>
    <svg class="card__edge" viewBox="0 0 540 310" aria-hidden="true">
      <rect x="8" y="8" width="524" height="294" rx="32" fill="none" stroke="var(--edge-blue)" stroke-width="16"/>
      <rect x="8" y="8" width="524" height="294" rx="32" fill="none" stroke="var(--edge-cyan)" stroke-width="16" stroke-dasharray="34 34"/>
    </svg>
    <div class="wordmark">
      <span class="wordmark__dot"></span>
      <span class="wordmark__name">
        <span class="wordmark__line wordmark__main">Azure Haven</span>
        <span class="wordmark__line wordmark__sub">of Northeast Florida</span>
      </span>
    </div>

    <div class="person">
      <p class="person__name"><span class="person__first">Mark</span> Ellison</p>
      <p class="person__title">general director</p>
      <p class="person__license">lic. 456789</p>
    </div>

    <ul class="contacts">
      <li class="contacts__item">
        <svg class="contacts__icon" viewBox="0 0 14 14" aria-hidden="true"><rect x="3.5" y="1" width="7" height="12" rx="1.5" fill="none" stroke="var(--accent-red)" stroke-width="1.6"/><circle cx="7" cy="11" r="0.8" fill="var(--accent-red)"/></svg>
        0123 45 6789
      </li>
      <li class="contacts__item">
        <svg class="contacts__icon" viewBox="0 0 14 14" aria-hidden="true"><path d="M3 1.5 L5.5 4 L4.2 5.6 C5 7.4 6.6 9 8.4 9.8 L10 8.5 L12.5 11 L11 12.6 C6.2 12.2 1.8 7.8 1.4 3 Z" fill="var(--accent-red)"/></svg>
        0123 45 6789
      </li>
      <li class="contacts__item">
        <svg class="contacts__icon" viewBox="0 0 14 14" aria-hidden="true"><rect x="1" y="3" width="12" height="8.5" fill="var(--accent-red)"/><path d="M1 3 L7 8 L13 3" fill="none" stroke="#fff" stroke-width="1.1"/></svg>
        mark@azurehavenfl.com
      </li>
      <li class="contacts__item">
        <svg class="contacts__icon" viewBox="0 0 14 14" aria-hidden="true"><circle cx="7" cy="7" r="5.6" fill="none" stroke="var(--accent-red)" stroke-width="1.3"/><ellipse cx="7" cy="7" rx="2.4" ry="5.6" fill="none" stroke="var(--accent-red)" stroke-width="1"/><line x1="1.4" y1="7" x2="12.6" y2="7" stroke="var(--accent-red)" stroke-width="1"/></svg>
        www.azurehavenfl.com
      </li>
    </ul>
  </section>

</main>
</body>
</html>
```